Capability Statement Document/Flyer

Take the existing words from the capability statement document (attached) and design a unique folder/flyer document for professional use. Maybe something like a trifold or bifold style. Use approved colours and logo as per the attached files.
Our company designs and builds small onshore gas processing plants.

```html
<!DOCTYPE html>
<html lang="en">
<head>
<meta charset="utf-8">
<title>Clarivo Capability Statement</title>
<link href="https://fonts.googleapis.com/css2?family=Open+Sans:ital,wght@0,400;0,600;0,700;1,400;1,600&display=swap" rel="stylesheet">
<style>
:root{
  --green:#1d6a56;
  --green-mid:#5f8d7f;
  --green-soft:#9fb3ab;
  --grey-light:#e1e5e2;
  --grey-mid:#a9aaa9;
  --backdrop:#d9dbda;
  --ink:#2b2b2b;
  --white:#ffffff;
}
*{box-sizing:border-box;margin:0;padding:0}
html,body{width:1200px;height:1156px;overflow:hidden}
body{background:var(--backdrop);font-family:"Open Sans",sans-serif;color:var(--ink);position:relative}
.spread{position:absolute;left:53px;width:1083px;height:510px;background:var(--white);overflow:hidden}
.spread-top{top:49px}
.spread-bottom{top:592px}
.abs{position:absolute}
.photo{position:absolute;background:linear-gradient(180deg,#9fb4cf 0%,#c9d3dc 55%,#b9a58a 80%,#8e7e6a 100%)}
.brand{position:absolute;background:var(--white);border:3px solid var(--grey-mid);color:var(--green);font-weight:700;display:flex;align-items:center;justify-content:center;letter-spacing:.5px;line-height:1}
.heading{position:absolute;color:var(--green);font-weight:600;font-size:13.5px;line-height:1}
.body-text{font-size:6.6px;line-height:8.7px}
.page-num{position:absolute;font-size:6.5px}

/* personnel page */
.personnel{position:absolute;left:34px;width:292px}
.person-table{width:100%;border-collapse:collapse;font-size:6.4px}
.person-table td{padding:1px 2px;line-height:8.2px;border-bottom:1.5px solid var(--white)}
.person-table .label{width:45px;color:var(--white);font-weight:700;background:var(--green)}
.person-table .label.role{background:var(--grey-mid)}
.person-table .value{background:var(--grey-light)}
.person-table .value.role{background:var(--white)}
.person-bio{margin-top:1px;padding-left:2px}

/* cover */
.cover{position:absolute;left:362px;top:0;width:721px;height:510px}
.cover-title{position:absolute;left:400px;top:134px;width:282px;text-align:center;color:var(--white);font-size:57px;line-height:58px;font-weight:400}
.cover-tagline{position:absolute;left:400px;top:394px;width:282px;text-align:center;color:var(--white);font-style:italic;font-size:17px;line-height:23px}
.cover-url{position:absolute;left:400px;top:465px;width:282px;text-align:center;color:var(--white);font-style:italic;font-size:11px}
.contact{position:absolute;color:var(--white);font-size:5.3px;line-height:7px}
.social{position:absolute;width:10px;height:10px;border:1px solid var(--white);border-radius:50%}

/* bottom spread */
.vision-box{position:absolute;left:75px;top:195px;width:224px;height:34px;background:var(--grey-light);border-radius:5px;text-align:center;font-size:6.4px;line-height:8px;padding-top:11px}
.principles-frame{position:absolute;left:99px;top:306px;width:188px;height:52px;border:1px solid var(--green);border-radius:4px}
.principles-title{position:absolute;left:119px;top:296px;width:138px;height:19px;background:var(--green);color:var(--white);font-weight:600;font-size:12px;line-height:19px;text-align:center;border-radius:3px}
.principles-list{position:absolute;left:129px;top:321px;font-size:6.4px;line-height:8.6px;list-style:none}
.principles-list span{display:inline-block;width:14px}
.role-tag{position:absolute;left:86px;width:84px;height:19px;color:var(--white);font-size:6.4px;font-weight:600;line-height:19px;padding-left:6px}
.org-label{position:absolute;font-size:5.8px;color:var(--green);text-align:center;width:60px}

.service-table{position:absolute;border-collapse:collapse;font-size:6.3px}
.service-table th{background:var(--green);color:var(--white);text-align:left;font-weight:600;font-size:7.5px;height:20px;padding-left:4px}
.service-table td{height:20.6px;padding:0 4px;line-height:8px;vertical-align:middle}
.service-table tr:nth-child(even) td{background:var(--grey-light)}
.service-table .fn{font-weight:600}

.roles-table{position:absolute;left:733px;top:155px;width:316px;border-collapse:collapse;font-size:6.3px}
.roles-table th{background:var(--green);color:var(--white);text-align:left;font-weight:600;font-size:7.5px;height:18px;padding-left:9px}
.roles-table td{height:19px;padding-left:9px}
.roles-table tr:nth-child(odd) td{background:var(--grey-light)}

.point-list{position:absolute;left:735px;list-style:none;font-size:6.4px;line-height:7.4px;width:205px}
.point-list li{position:relative;padding-left:11px;margin-bottom:4.8px}
.point-list li::before{content:"";position:absolute;left:0;top:1px;width:5px;height:5px;border-radius:50%;background:var(--green)}
.point-list.challenges li::before{background:var(--green-soft)}
</style>
</head>
<body>

<!-- TOP SPREAD -->
<section class="spread spread-top">
  <div class="photo" style="left:0;top:0;width:362px;height:107px" role="img" aria-label="Solar panel arrays beside a small onshore gas processing plant"></div>
  <div class="brand" style="left:35px;top:25px;width:104px;height:25px;font-size:18px">CLARIVO</div>

  <h2 class="heading" style="left:34px;top:132px">Key Clarivo Personnel</h2>

  <div class="personnel" style="top:155px">
    <table class="person-table">
      <tr><td class="label">Name:</td><td class="value">Martin Hale</td></tr>
      <tr><td class="label role">Role:</td><td class="value role">Executive Director</td></tr>
      <tr><td class="label">35yrs Exp:</td><td class="value">Harbour Petroleum, Kestrel Energy, TRSC, Ridgeline Energy</td></tr>
    </table>
    <p class="body-text person-bio">Extensive global energy industry experience, from frontline O&amp;M to the boardroom. Respected ‘C Suite’ leader with a track record of building high performing teams that deliver outstanding results.</p>
  </div>

  <div class="personnel" style="top:224px">
    <table class="person-table">
      <tr><td class="label">Name:</td><td class="value">Douglas Reid</td></tr>
      <tr><td class="label role">Role:</td><td class="value role">Technical Director</td></tr>
      <tr><td class="label">39yrs Exp:</td><td class="value">Harbour Petroleum, Kestrel Energy, Desert Petroleum Co.,<br>NPX, MG Group, QFG, TRSC, Ridgeline Energy</td></tr>
    </table>
    <p class="body-text person-bio">Highly skilled &amp; experienced operations &amp; project management professional with 39 years’ experience in the global oil &amp; gas industry delivering multiple projects and establishing best in class operational assets. Deep knowledge of project management, construction, commissioning &amp; start-up including a global functional assurance role.</p>
  </div>

  <div class="personnel" style="top:311px">
    <table class="person-table">
      <tr><td class="label">Name:</td><td class="value">Graham Toller</td></tr>
      <tr><td class="label role">Role:</td><td class="value role">Commercial Director</td></tr>
      <tr><td class="label">40yrs Exp:</td><td class="value">Eastshore, ORVEX, NPX, TRSC, Ridgeline Energy</td></tr>
    </table>
    <p class="body-text person-bio">Senior Logistics &amp; Supply Chain Manager / Procurement Manager with strong operational, commercial, project management, negotiating &amp; relationship building skills. Experienced in operating complex and diverse logistics operations, significantly improving service levels whilst reducing cost.</p>
  </div>

  <div class="personnel" style="top:389px">
    <table class="person-table">
      <tr><td class="label">Name:</td><td class="value">Ian Barrow</td></tr>
      <tr><td class="label role">Role:</td><td class="value role">Operations Director</td></tr>
      <tr><td class="label">27yrs Exp:</td><td class="value">NPX, MG Group, QFG, TRSC, Ridgeline Energy</td></tr>
    </table>
    <p class="body-text person-bio">27 years’ success leading operations, maintenance and commissioning teams on onshore and offshore oil and gas production platforms, FPSOs, gas processing, coal seam gas, refrigeration facilities, and chemical refineries.<br>Results driven and enthusiastic Leader with a proven track record of delivery.</p>
  </div>

  <div class="page-num" style="left:190px;top:487px">5</div>

  <!-- cover -->
  <div class="cover">
    <div class="photo" style="left:0;top:0;width:721px;height:510px;background:linear-gradient(180deg,#51648d 0%,#8ea6c6 35%,#c9d2dc 60%,#b8a68c 78%,#8d7d68 100%)" role="img" aria-label="Solar panel arrays framing an onshore gas processing plant under a clear sky"></div>
    <svg class="abs" style="left:0;top:0" width="721" height="510" viewBox="0 0 721 510" aria-hidden="true">
      <polygon points="0,340 503,380 0,435" fill="#b5b6b8"/>
      <polygon points="0,435 721,332 721,510 0,510" fill="#1d6a56"/>
    </svg>
    <div class="brand" style="left:435px;top:61px;width:212px;height:52px;font-size:38px">CLARIVO</div>
    <div class="brand" style="left:73px;top:191px;width:212px;height:51px;font-size:38px">CLARIVO</div>
    <h1 class="cover-title">Capability Statement</h1>
    <p class="cover-tagline">Simplify Project Execution,<br>Streamline Operations</p>
    <p class="cover-url">www.clarivo.com.au</p>

    <svg class="abs" style="left:20px;top:467px" width="8" height="10" viewBox="0 0 8 10" aria-hidden="true"><path d="M4 0a3.4 3.4 0 0 0-3.4 3.4C.6 6 4 9.5 4 9.5S7.4 6 7.4 3.4A3.4 3.4 0 0 0 4 0z" fill="none" stroke="#fff" stroke-width=".8"/><circle cx="4" cy="3.4" r="1.1" fill="#fff"/></svg>
    <p class="contact" style="left:34px;top:465px">Street, 234 Lorem Ipsum,<br>Big Vallejo, California, 00917</p>

    <svg class="abs" style="left:159px;top:437px" width="9" height="9" viewBox="0 0 10 10" aria-hidden="true"><path d="M2 1l2 2-1 1.2c.6 1.3 1.5 2.2 2.8 2.8L7 6l2 2-1.3 1.5C4.5 9.3.7 5.5.5 2.3z" fill="#fff"/></svg>
    <p class="contact" style="left:181px;top:434px">+00 1234 567 8900<br>+00 1234 567 8900</p>
    <svg class="abs" style="left:158px;top:456px" width="10" height="7" viewBox="0 0 10 7" aria-hidden="true"><rect x=".4" y=".4" width="9.2" height="6.2" fill="none" stroke="#fff" stroke-width=".7"/><path d="M.4.4 5 4 9.6.4" fill="none" stroke="#fff" stroke-width=".7"/></svg>
    <p class="contact" style="left:181px;top:453px">yourmailadress@domain.com<br>secondmail@domain.com</p>
    <svg class="abs" style="left:159px;top:473px" width="9" height="9" viewBox="0 0 10 10" aria-hidden="true"><circle cx="5" cy="5" r="4.4" fill="none" stroke="#fff" stroke-width=".7"/><ellipse cx="5" cy="5" rx="2" ry="4.4" fill="none" stroke="#fff" stroke-width=".7"/><path d="M.6 5h8.8" stroke="#fff" stroke-width=".7"/></svg>
    <p class="contact" style="left:181px;top:474px">www.clarivo.com.au</p>

    <div class="brand" style="left:299px;top:429px;width:50px;height:12px;font-size:8.5px;border-width:1.5px">CLARIVO</div>
    <p class="contact" style="left:299px;top:449px;font-size:6.4px">Follow us</p>
    <span class="social" style="left:299px;top:461px"></span>
    <span class="social" style="left:319px;top:461px"></span>
    <span class="social" style="left:338px;top:461px"></span>
  </div>
</section>

<!-- BOTTOM SPREAD -->
<section class="spread spread-bottom">
  <div class="photo" style="left:0;top:0;width:1083px;height:106px" role="img" aria-label="Wide view of solar arrays and gas processing plant pipework"></div>
  <div class="brand" style="left:35px;top:81px;width:104px;height:25px;font-size:18px">CLARIVO</div>

  <!-- page 2 -->
  <h2 class="heading" style="left:34px;top:131px">Who are Clarivo?</h2>
  <p class="abs body-text" style="left:34px;top:152px;width:307px"><b><i>Clarivo</i></b> are a highly experienced team of Executive, Project, Construction, Commissioning and Operations specialists who combine deep technical knowledge with proven leadership to deliver unique <b>Project Delivery Partner</b> services to organisations in Australia.</p>
  <svg class="abs" style="left:176px;top:185px" width="22" height="18" viewBox="0 0 22 18" aria-hidden="true"><rect x="4" y="1" width="4" height="8" rx="1.5" fill="#1d6a56"/><rect x="14" y="1" width="4" height="8" rx="1.5" fill="#1d6a56"/><rect x="8" y="5" width="6" height="3" fill="#1d6a56"/><circle cx="6" cy="12" r="4.5" fill="none" stroke="#1d6a56" stroke-width="2.2"/><circle cx="16" cy="12" r="4.5" fill="none" stroke="#1d6a56" stroke-width="2.2"/></svg>
  <div class="vision-box">Our vision is straightforward:<br><b><i>Simplify Project Execution, Streamline Operations.</i></b></div>

  <h2 class="heading" style="left:34px;top:237px">What is a Project Delivery Partner?</h2>
  <p class="abs body-text" style="left:34px;top:258px;width:310px">A Project Delivery Partner (PDP) provides integrated project management along with technical, commercial and delivery support services to help an organisation successfully deliver a project. The PDP acts as the owner’s team while the owner retains accountability and key decision-making authority.</p>

  <div class="principles-frame"></div>
  <svg class="abs" style="left:86px;top:320px" width="26" height="26" viewBox="0 0 26 26" aria-hidden="true"><circle cx="13" cy="13" r="12" fill="#fff" stroke="#1d6a56" stroke-width=".8"/><rect x="10" y="7" width="6" height="3.5" fill="none" stroke="#1d6a56" stroke-width=".7"/><path d="M13 10.5v3M7 13.5h12M7 13.5v2M13 13.5v2M19 13.5v2" fill="none" stroke="#1d6a56" stroke-width=".7"/><rect x="5" y="15.5" width="4" height="3" fill="none" stroke="#1d6a56" stroke-width=".7"/><rect x="11" y="15.5" width="4" height="3" fill="none" stroke="#1d6a56" stroke-width=".7"/><rect x="17" y="15.5" width="4" height="3" fill="none" stroke="#1d6a56" stroke-width=".7"/></svg>
  <div class="principles-title">PDP Core Principles:</div>
  <ol class="principles-list">
    <li><span>1.</span>Owner controls the project</li>
    <li><span>2.</span>PDP enables delivery &amp; provides assurance</li>
    <li><span>3.</span>Contractors execute the work</li>
  </ol>

  <div class="role-tag" style="top:378px;background:var(--green)">Owner</div>
  <div class="role-tag" style="top:413px;background:var(--green-mid)">Project Delivery Partner</div>
  <div class="role-tag" style="top:449px;background:var(--green-soft)">Contractors</div>
  <svg class="abs" style="left:0;top:0" width="361" height="510" viewBox="0 0 361 510" aria-hidden="true">
    <path d="M170 382.5l5 5-5 5z" fill="#1d6a56"/>
    <path d="M170 417.5l5 5-5 5z" fill="#5f8d7f"/>
    <path d="M170 454l5 5-5 5z" fill="#9fb3ab"/>
    <path d="M237 399v14M237 436v6M199 442h75M199 442v8M237 442v8M274 442v8" fill="none" stroke="#9fb3ab" stroke-width=".7" stroke-dasharray="1.5 1.2"/>
    <circle cx="237" cy="380" r="5" fill="#1d6a56"/>
    <circle cx="237" cy="422" r="5" fill="#5f8d7f"/>
    <circle cx="199" cy="459" r="5" fill="#9fb3ab"/>
    <circle cx="237" cy="459" r="5" fill="#9fb3ab"/>
    <circle cx="274" cy="459" r="5" fill="#9fb3ab"/>
  </svg>
  <div class="org-label" style="left:207px;top:392px">OPERATOR XYZ</div>
  <div class="org-label" style="left:207px;top:429px">CLARIVO</div>
  <div class="org-label" style="left:169px;top:470px">Engineering</div>
  <div class="org-label" style="left:207px;top:470px">Suppliers</div>
  <div class="org-label" style="left:244px;top:470px">Execution</div>
  <div class="page-num" style="left:191px;top:487px">2</div>

  <!-- page 3 -->
  <h2 class="heading" style="left:383px;top:131px">PDP Objective:</h2>
  <p class="abs body-text" style="left:383px;top:155px;width:318px">Deliver the project safely, on schedule, within budget and ready for operations; providing owner capability throughout the project lifecycle.</p>
  <table class="service-table" style="left:383px;top:190px;width:316px">
    <tr><th style="width:18px">#</th><th style="width:90px">Function</th><th>Clarivo Service</th></tr>
    <tr><td>1</td><td class="fn">Project Management</td><td>Planning, Reporting &amp; Delivery Leadership from Concept to Completion</td></tr>
    <tr><td>2</td><td class="fn">Engineering</td><td>Concept Selection, Design Coordination, Technical Assurance &amp; Value Engineering</td></tr>
    <tr><td>3</td><td class="fn">Procurement</td><td>Contracting Strategy, Tender Process &amp; Supplier/Contractor Management</td></tr>
    <tr><td>4</td><td class="fn">Approvals</td><td>Land Access, Regulator Engagement, Safety Case, Permits &amp; Licenses</td></tr>
    <tr><td>5</td><td class="fn">Cost Control</td><td>Budget Development, Forecasting &amp; Management</td></tr>
    <tr><td>6</td><td class="fn">Scheduling</td><td>Master Schedule Development, WBS, Resource Allocation, Monitoring &amp; Updating</td></tr>
    <tr><td>7</td><td class="fn">Risk Management</td><td>Risk Register, Identification, Mitigation &amp; Reporting</td></tr>
    <tr><td>8</td><td class="fn">Governance</td><td>Framework, Stage Gates, Change control, Reporting &amp; Decision Support</td></tr>
    <tr><td>9</td><td class="fn">Construction</td><td>Management &amp; Coordination of Contractor Execution Teams</td></tr>
    <tr><td>10</td><td class="fn">Commissioning &amp; Start-up</td><td>Lead Commissioning &amp; Start-up, Completions System, Bring the Facility to Steady-State</td></tr>
    <tr><td>11</td><td class="fn">Operations Readiness</td><td>People &amp; Organisation, Process &amp; Procedures, Systems &amp; Technology</td></tr>
    <tr><td>12</td><td class="fn">Operations &amp; Maintenance</td><td>Monitor &amp; Operate Asset, Minimize Downtime, Lowest Possible OPEX for Owner</td></tr>
  </table>
  <div class="page-num" style="left:540px;top:487px">3</div>

  <!-- page 4 -->
  <h2 class="heading" style="left:733px;top:131px">PDP Roles &amp; Responsibilities:</h2>
  <table class="roles-table">
    <tr><th style="width:151px">Owner</th><th>Clarivo Service</th></tr>
    <tr><td>Sets Project Objectives</td><td>Develops Delivery Plans</td></tr>
    <tr><td>Approves Major Decisions</td><td>Provides Recommendations</td></tr>
    <tr><td>Holds Project Risk</td><td>Identifies and Manages Risks</td></tr>
    <tr><td>Awards Contracts</td><td>Manages Contractor Interfaces</td></tr>
    <tr><td>Provides Funding</td><td>Monitors Cost and Schedule Performance</td></tr>
  </table>

  <div class="photo" style="left:937px;top:272px;width:146px;height:204px;background:linear-gradient(180deg,#a8bdd6 0%,#cfd6dc 40%,#9aa3a6 70%,#b59c7c 100%)" role="img" aria-label="Close view of gas processing plant pipework and valves"></div>

  <h2 class="heading" style="left:733px;top:280px">PDP Benefits:</h2>
  <ul class="point-list" style="top:306px">
    <li>Provides owners with access to experienced project delivery capability</li>
    <li>Improved project controls and governance</li>
    <li>Greater flexibility than traditional EPC delivery</li>
    <li>Enhanced visibility and management of cost, schedule and risk</li>
    <li>Scalable resources aligned with project phases</li>
  </ul>

  <h2 class="heading" style="left:733px;top:383px">PDP Challenges:</h2>
  <ul class="point-list challenges" style="top:408px">
    <li>Owner retains significant delivery risk</li>
    <li>Requires clear governance and decision-making processes</li>
    <li>Multiple contractor interfaces require strong coordination</li>
    <li>Success depends on collaborative Owner-PDP relationship</li>
  </ul>
  <p class="abs body-text" style="left:733px;top:462px">For More Information Contact: <b>directors@clarivo.com.au</b></p>
  <div class="page-num" style="left:889px;top:487px">4</div>
</section>

</body>
</html>
```